Label design

Description
I want you to design a label for a skin care product line. I’ve provide the picture of the jar we are using along with the logo. Please note that the logo is available in different colors as well. (See attached) I would like the label to be very clean and straight to the point. Here is some info that I would like to see on the label:
240G
Net wt 8.0z

The content of the jar can be refer to as:

Body cream
Crème de corps
Body butter
Fade cream
Skin tone cream
Lotion pour le corps
Clarifying Body cream
Lightening Cream

The content is also made an exotic component that: “Extraits de noisette de palmiers” meaning nuts extract.

The brand NAME is: Miravé
The tag line is: 

Industry/Entity Type

Skin Care Product

```html
<!DOCTYPE html>
<html lang="fr">
<head>
<meta charset="utf-8">
<title>Miravé — Crème de corps label</title>
<link rel="stylesheet" href="https://fonts.googleapis.com/css2?family=Andika&family=Questrial&display=swap">
<style>
  :root {
    --backdrop: #eef1f3;
    --label-white: #ffffff;
    --label-edge: #c9d3d8;
    --brand-orange: #f57f17;
    --swoosh-light: #ffb300;
    --swoosh-deep: #ff7800;
    --type-white: #ffffff;
  }
  html, body {
    margin: 0;
    padding: 0;
    width: 973px;
    height: 1200px;
    overflow: hidden;
    background: var(--backdrop);
  }
  .canvas {
    position: relative;
    width: 973px;
    height: 1200px;
  }
  .label {
    position: absolute;
    left: 56px;
    top: 268px;
    width: 860px;
    height: 663px;
    background: var(--label-white);
    border: 1px solid var(--label-edge);
    border-radius: 6px;
    overflow: hidden;
  }
  .swoosh {
    position: absolute;
    left: 0;
    top: 0;
    width: 860px;
    height: 663px;
  }
  .brand {
    position: absolute;
    left: 400px;
    top: 190px;
    width: 440px;
    text-align: center;
  }
  .brand-name {
    margin: 0;
    font-family: "Questrial", sans-serif;
    font-weight: 400;
    font-size: 96px;
    line-height: 1;
    color: var(--brand-orange);
  }
  .product {
    position: absolute;
    left: 237px;
    top: 510px;
    width: 400px;
    text-align: center;
    color: var(--type-white);
  }
  .product-name {
    margin: 0;
    font-family: "Andika", sans-serif;
    font-weight: 400;
    font-size: 46px;
    line-height: 1.2;
  }
  .net-weight {
    margin: 8px 0 0;
    font-family: "Questrial", sans-serif;
    font-size: 38px;
    line-height: 1.2;
  }
</style>
</head>
<body>
<main class="canvas">
  <section class="label">
    <svg class="swoosh" viewBox="0 0 860 663" aria-hidden="true">
      <defs>
        <linearGradient id="swooshFill" x1="0" y1="0" x2="1" y2="0.3">
          <stop offset="0" stop-color="var(--swoosh-light)"/>
          <stop offset="1" stop-color="var(--swoosh-deep)"/>
        </linearGradient>
      </defs>
      <path d="M105 506 Q 500 320 780 663 L 182 663 Q 135 590 105 506 Z" fill="url(#swooshFill)"/>
    </svg>
    <div class="brand">
      <h1 class="brand-name">Miravé</h1>
    </div>
    <div class="product">
      <h2 class="product-name">Crème de corps</h2>
      <p class="net-weight">Net wt 8.0z</p>
    </div>
  </section>
</main>
</body>
</html>
```